Digital Billboard Design: Winter Sales Event

I own a boutique furniture store in Calgary, AB (maplewoven.ca) and I am looking to advertise our winter sale event on a new curved digital billboard (specs attached including required file type).

I have this billboard rented for 52-weeks so I will be looking to change the design every 4-weeks (i.e. this is intended to be an ongoing project).

The objective of this first billboard is to raise awareness around our annual winter sales event. The store itself is only a few blocks from the billboard so those commuting into downtown are just a short drive from the store.

I am looking for a fresh, clean, contemporary look that will grab your attention as you drive into downtown Calgary without presenting to much info so as to be distracting (and overwhelming -- the billboard does not need to contain all info on my current marketing material). I should also note that the store caters to a higher-end, more sophisticated clientele so the graphics need to reflect the brand (i.e. we are not Brenton Furniture or Couch Depot!).

I have attached three files:

Billboard specs
Current marketing material advertising sale (and all relevant data)
An idea that is from an American furniture store that I think is interesting

Target Market(s)

Upper middle class, sophisticated client who appreciates the finer things in life.

Industry/Entity Type

Furniture Store

Font styles to use
Sans Serif

Requirements
Must have
• Company Logo
• Winter Sales Event - 20 to 60% off
• Address: 3847 22nd Ave SW
Nice to have
• Image of furniture -- see our website www.maplewoven.ca -- any photo from this site can be used
Should not have
• Too much text or visual distration

```html
<!DOCTYPE html>
<html lang="en">
<head>
<meta charset="utf-8">
<title>Maple Woven – Winter Sales Event Billboards</title>
<link rel="stylesheet" href="https://fonts.googleapis.com/css2?family=Montserrat:wght@300;400&display=swap">
<style>
  :root {
    --page-bg: #ffffff;
    --frame: #333333;
    --ink: #ffffff;
    --bg-base: #647673;
    --bg-teal: #6f8a8e;
    --bg-olive: #6d7a5c;
    --bg-deep: #44544f;
    --bg-light: #8a9a96;
  }
  * { margin: 0; padding: 0; box-sizing: border-box; }
  html, body {
    width: 1200px; height: 1000px; overflow: hidden;
    background: var(--page-bg);
    font-family: "Montserrat", sans-serif;
    color: var(--ink);
  }
  .sheet {
    position: absolute; left: 34px; top: 36px;
    width: 1135px; height: 935px;
    border: 3px solid var(--frame);
  }
  .billboard {
    position: absolute; width: 875px; height: 406px; overflow: hidden;
    background:
      radial-gradient(circle at 30% 35%, rgba(140,170,175,.45) 0, transparent 18%),
      radial-gradient(circle at 62% 55%, rgba(120,150,170,.4) 0, transparent 20%),
      radial-gradient(circle at 20% 75%, rgba(110,130,90,.55) 0, transparent 30%),
      radial-gradient(circle at 85% 20%, rgba(150,165,160,.45) 0, transparent 30%),
      radial-gradient(circle at 50% 100%, var(--bg-deep) 0, transparent 45%),
      linear-gradient(135deg, var(--bg-olive) 0%, var(--bg-base) 40%, var(--bg-teal) 75%, var(--bg-light) 100%);
  }
  .billboard--stacked { left: 163px; top: 85px; }
  .billboard--feature { left: 163px; top: 515px; width: 876px; }
  .billboard > * { position: absolute; line-height: 1; text-align: center; white-space: nowrap; }
  .brand { font-weight: 400; letter-spacing: .17em; }
  .address { font-weight: 300; }
  .light { font-weight: 300; }
  .regular { font-weight: 400; }
  .divider { width: 2px; background: var(--ink); opacity: .9; }

  /* stacked layout */
  .billboard--stacked .brand { left: 0; width: 875px; top: 40px; font-size: 48px; }
  .billboard--stacked .address { left: 0; width: 875px; top: 94px; font-size: 27px; }
  .billboard--stacked .event-title { left: 25px; width: 400px; top: 180px; }
  .billboard--stacked .offer { left: 447px; width: 400px; top: 168px; }
  .billboard--stacked .divider { left: 436px; top: 173px; height: 180px; }

  .event-title .line-sm { display: block; font-size: 44px; }
  .event-title .line-lg { display: block; font-size: 104px; font-weight: 300; margin-top: -4px; }
  .event-title .line-end { display: block; font-size: 29px; margin-top: 2px; }

  .offer .get { display: block; font-size: 56px; font-weight: 300; }
  .offer .amount { display: block; font-size: 92px; font-weight: 400; margin-top: -2px; }
  .offer .off { display: block; font-size: 56px; font-weight: 300; margin-top: -4px; }

  /* feature layout */
  .furniture-image {
    left: 54px; top: 58px; width: 306px; height: 146px;
    border-radius: 60px 60px 10px 10px;
    background: linear-gradient(180deg, rgba(255,255,255,.14), rgba(255,255,255,.05));
  }
  .billboard--feature .event-title { left: 9px; width: 400px; top: 218px; }
  .billboard--feature .event-title .line-sm { font-size: 46px; }
  .billboard--feature .event-title .line-lg { font-size: 106px; }
  .billboard--feature .divider { left: 409px; top: 48px; height: 312px; }
  .billboard--feature .brand { left: 434px; width: 420px; top: 66px; font-size: 38px; }
  .billboard--feature .address { left: 434px; width: 420px; top: 108px; font-size: 20px; }
  .billboard--feature .offer-line { left: 434px; width: 420px; top: 164px; }
  .offer-line .get { font-size: 52px; font-weight: 300; }
  .offer-line .amount { font-size: 74px; font-weight: 400; }
  .billboard--feature .off { left: 434px; width: 400px; top: 228px; font-size: 54px; font-weight: 300; }
  .billboard--feature .ends { left: 434px; width: 420px; top: 310px; font-size: 30px; }
</style>
</head>
<body>
  <div class="sheet"></div>

  <section class="billboard billboard--stacked">
    <div class="brand">MAPLE WOVEN</div>
    <div class="address">3847 22ND AVE SW, CALGARY, AB</div>
    <div class="event-title">
      <span class="line-sm"><span class="regular">WINTER</span> <span class="light">SALES</span></span>
      <span class="line-lg">EVENT</span>
      <span class="line-end"><span class="light">ENDS</span> <span class="regular">JANUARY 31ST</span></span>
    </div>
    <div class="divider"></div>
    <div class="offer">
      <span class="get">GET</span>
      <span class="amount">20-60%</span>
      <span class="off">OFF</span>
    </div>
  </section>

  <section class="billboard billboard--feature">
    <div class="furniture-image" role="img" aria-label="Line illustration of a sofa"></div>
    <div class="event-title">
      <span class="line-sm"><span class="regular">WINTER</span> <span class="light">SALES</span></span>
      <span class="line-lg">EVENT</span>
    </div>
    <div class="divider"></div>
    <div class="brand">MAPLE WOVEN</div>
    <div class="address">3847 22ND AVE SW, CALGARY, AB</div>
    <div class="offer-line"><span class="get">GET</span> <span class="amount">20-60%</span></div>
    <div class="off">OFF</div>
    <div class="ends"><span class="light">ENDS</span> <span class="regular">JANUARY 31ST</span></div>
  </section>
</body>
</html>
```